"Word Cloud" lists of countries, by decade, who have adopted women's suffrage

The winning designer will (eventually, but not necessarily within this project--see "Nice to Haves", below) design a total of eight images, based on the eight lists of countries (see attached files) in order, by decade, that they adopted women's suffrage.

One of the the attached images is a screen shot of five pages of the book KITE: Notes Toward a Borderless Tomorrow, showing how these lists are presently arranged on 6"x9" pages.

We essentially want to spice up these 8 lists and make them more fun to look at, for the reader.

Target Market(s)

General audience. People who want to make a difference. People who want to do something to change the world, and want to read a book about how we can actually do it.

Industry/Entity Type

Political

Font styles to use
Serif
Sans Serif
Decorative
Script

Requirements
Must have
• At least two initial designs, one for each of the two largest lists (lists 5 and 6). All country names must be spelled correctly. A WORD doc has been provided with all the text you need to work with. An EXAMPLE word cloud has been provided for inspiration. The look and feel of these "Country Clouds" wants to go all over the place, but all names should be (at least somewhat) readable.
• IMPORTANT ELEMENTS: (1) There are a few places where current countries were just one, when they got women's suffrage. Keep this info intact, together, in the cloud. EXAMPLE (from list 6):
•  British Leeward Islands (remove ", including today’s:", but keep together with)
•  Antigua and Barbuda
•  British Virgin Islands
•  Montserrat
•  Saint Kitts and Nevis
•  Anguilla
• (2) The names of the countries should stay in roughly the same order as found in the lists, but laid out (very) roughly right to left and then top to bottom, loosely akin to the standard flow of text written in the latin alphabet. It is fine to alter this standard in minor ways to achieve a better look to the design. Just don't move a country found at the top of one list into the middle of that list or down to the bottom, etc.
• These country clouds will be printed in black and white, so keep the designs greyscale.
• These "country clouds" should be 4.5" in width.The largest country clouds, with the most countries found in them, should not exceed 6" in length.
Nice to have
• (Eventually) all 8 lists in the form of "Country Clouds"---that are playful, but with serious elements. Pull up a list of countries by population, have the 20 biggest use the biggest font sizes. Use many different fonts, mix it up! Essentially, these 8 lists all want to become word clouds, with each nation's full name as its own "word." See example cloud.
• Though having all 8 lists in clouds at the end of this project is "nice to have," the winner for this design might simply produce 2 such clouds, along with a cost estimate attached to the submitted design for what they would charge to complete the other 6 clouds.
Should not have
• Do NOT include the textual transitions found between the lists, in the screen shot or word doc. They are there just to help you see how the different graphics will be used and what will go either before or after them.
• No need to use bullet points.

```html
<!DOCTYPE html>
<html lang="en">
<head>
<meta charset="utf-8">
<title>Country Cloud — Women's Suffrage</title>
<link rel="stylesheet" href="https://fonts.googleapis.com/css2?family=Anton&family=Archivo+Black&family=Cinzel:wght@400;700&family=Libre+Baskerville:ital,wght@0,400;0,700;1,400&family=Montserrat:ital,wght@0,400;0,500;0,700;0,800;1,700&family=Oswald:wght@500;700&family=Playball&family=Playfair+Display:ital,wght@0,400;1,400&display=swap">
<style>
  :root {
    --paper: #ffffff;
    --ink: #111111;
  }
  html, body {
    margin: 0;
    padding: 0;
    width: 900px;
    height: 1200px;
    overflow: hidden;
    background: var(--paper);
  }
  .country-cloud {
    position: relative;
    width: 900px;
    height: 1200px;
    background: var(--paper);
    color: var(--ink);
    overflow: hidden;
  }
  .country {
    position: absolute;
    margin: 0;
    line-height: 1;
    white-space: nowrap;
  }
  .rotate-up   { transform-origin: 0 0; transform: rotate(-90deg) translateX(-100%); }
  .rotate-down { transform-origin: 0 0; transform: rotate(90deg) translateY(-100%); }

  .sans      { font-family: "Montserrat", sans-serif; }
  .condensed { font-family: "Anton", sans-serif; }
  .narrow    { font-family: "Oswald", sans-serif; }
  .heavy     { font-family: "Archivo Black", sans-serif; }
  .serif     { font-family: "Libre Baskerville", serif; }
  .didone    { font-family: "Playfair Display", serif; }
  .caps      { font-family: "Cinzel", serif; }
  .script    { font-family: "Playball", cursive; }

  .bahamas      { left: 104px; top: 36px;  font-size: 24px; font-weight: 700; }
  .gambia       { left: 465px; top: 36px;  font-size: 35px; }
  .uganda       { left: 774px; top: 26px;  font-size: 84px; }
  .rwanda       { left: 686px; top: 38px;  font-size: 60px; font-weight: 500; }
  .cyprus       { left: 42px;  top: 108px; font-size: 26px; font-weight: 800; }
  .paraguay     { left: 32px;  top: 234px; font-size: 40px; font-weight: 500; }
  .burundi      { left: 99px;  top: 98px;  font-size: 68px; }
  .malawi       { left: 372px; top: 102px; font-size: 82px; font-weight: 500; }
  .tonga        { left: 120px; top: 170px; font-size: 34px; }
  .sierra-leone { left: 112px; top: 222px; font-size: 39px; font-weight: 500; }
  .mauritania   { left: 418px; top: 208px; font-size: 40px; }
  .algeria      { left: 110px; top: 268px; font-size: 100px; font-weight: 800; }
  .monaco       { left: 566px; top: 330px; font-size: 28px; }
  .zambia       { left: 112px; top: 408px; font-size: 52px; font-weight: 500; }
  .afghanistan  { left: 356px; top: 382px; font-size: 84px; }
  .figi         { left: 776px; top: 494px; font-size: 38px; font-weight: 800; }
  .congo-big    { left: 6px;   top: 458px; font-size: 140px; font-weight: 700; }
  .eq-guinea    { left: 186px; top: 478px; font-size: 50px; font-weight: 500; }
  .iran         { left: 268px; top: 468px; font-size: 220px; }
  .kenya        { left: 654px; top: 492px; font-size: 92px; font-style: italic; }
  .sudan        { left: 756px; top: 530px; font-size: 94px; font-weight: 500; }
  .morocco      { left: 268px; top: 676px; font-size: 86px; }
  .papua        { left: 264px; top: 828px; font-size: 45px; }
  .botswana     { left: 288px; top: 870px; font-size: 38px; font-weight: 700; font-style: italic; }
  .lesotho      { left: 588px; top: 870px; font-size: 37px; }
  .tuvalu       { left: 798px; top: 866px; font-size: 26px; }
  .zaire        { left: 140px; top: 920px; font-size: 70px; font-weight: 500; }
  .south-yemen  { left: 24px;  top: 1012px; font-size: 32px; font-weight: 700; }
  .swaziland    { left: 450px; top: 1034px; font-size: 34px; font-weight: 700; }
  .kiribati     { left: 696px; top: 1018px; font-size: 34px; font-style: italic; }
  .nauru        { left: 288px; top: 1064px; font-size: 30px; }
  .andorra      { left: 696px; top: 1068px; font-size: 27px; font-weight: 800; letter-spacing: 1px; }
</style>
</head>
<body>
  <main class="country-cloud" aria-label="Countries that adopted women's suffrage in this decade">
    <p class="country sans bahamas">Bahamas</p>
    <p class="country condensed gambia">The Gambia</p>
    <p class="country condensed rotate-up uganda">UGANDA</p>
    <p class="country sans rotate-up rwanda">Rwanda</p>
    <p class="country sans rotate-up cyprus">CYPRUS</p>
    <p class="country sans rotate-up paraguay">Paraguay</p>
    <p class="country script burundi">Burundi</p>
    <p class="country sans malawi">Malawi</p>
    <p class="country serif tonga">Tonga</p>
    <p class="country sans sierra-leone">Sierra Leone</p>
    <p class="country heavy mauritania">Mauritania</p>
    <p class="country sans algeria">Algeria</p>
    <p class="country caps monaco">Monaco</p>
    <p class="country sans zambia">Zambia</p>
    <p class="country serif afghanistan">Afghanistan</p>
    <p class="country sans figi">Figi</p>
    <p class="country sans rotate-up congo-big">Congo</p>
    <p class="country narrow rotate-up eq-guinea">Equatorial Guinea</p>
    <p class="country condensed iran">IRAN</p>
    <p class="country didone rotate-up kenya">Kenya</p>
    <p class="country sans rotate-up sudan">Sudan</p>
    <p class="country didone morocco">Morocco</p>
    <p class="country sans papua">Papua New Guinea</p>
    <p class="country sans botswana">Botswana</p>
    <p class="country sans lesotho">Lesotho</p>
    <p class="country narrow rotate-down tuvalu">Tuvalu</p>
    <p class="country sans zaire">Zaire (Congo)</p>
    <p class="country narrow south-yemen">SOUTH YEMEN (YEMEN)</p>
    <p class="country serif swaziland">Swaziland</p>
    <p class="country didone kiribati">Kirbati</p>
    <p class="country didone nauru">Nauru</p>
    <p class="country sans andorra">Andorra</p>
  </main>
</body>
</html>
```